Labels for fruit liqueur bottles

We are looking for a visual identity based on our logo, for fruit liqueur labels. To date, we have different liqueurs such as: lemon liqueur, orange liqueurs, mandarin liqueurs, grapefruit liqueurs. We will then create other liqueurs such as strawberry, apple or even apricot. Our goal is to have a single visual that we can adapt in different colors depending on the fruit used.

On the label there should be:
the logo
homemade
the name of the fruit (which can be changed depending on the product)
swiss-made
50cl
21°

Colors

Designer to choose colors to be used in the design.

Requirements
Must have
• a visual of liquor bottle labels, with the possibility of changing the background colors, depending on the fruit used
Nice to have
• something modern and nice to look at. We must be able to read the basic fruit in the blink of an eye. it is also possible to have a black or white or colored label background.

```html
<!DOCTYPE html>
<html lang="fr">
<head>
<meta charset="utf-8">
<title>Liqueur de Grappefruits – étiquette</title>
<link rel="stylesheet" href="https://fonts.googleapis.com/css2?family=Roboto+Condensed:wght@400;700&family=Roboto:wght@500&display=swap">
<style>
  :root {
    --backdrop: #e9cbbb;
    --label-border: #ffffff;
    --pink-top: #ef7d8d;
    --pink-bottom: #f890a2;
    --brand-orange: #ec4f12;
    --band-green: #a9c43a;
    --band-yellow: #f4a52a;
    --white: #ffffff;
  }
  * { box-sizing: border-box; margin: 0; padding: 0; }
  html, body {
    width: 1200px; height: 694px; overflow: hidden;
    background: var(--backdrop);
  }
  .stage {
    width: 1200px; height: 694px;
    display: flex; align-items: center; justify-content: center;
  }
  .label {
    width: 336px; height: 582px;
    background: var(--label-border);
    padding: 6px;
  }
  .label-body {
    position: relative;
    width: 100%; height: 100%;
    background: linear-gradient(180deg, var(--pink-top) 0%, var(--pink-bottom) 45%, var(--pink-bottom) 100%);
    overflow: hidden;
  }
  .title-card {
    position: absolute; left: 67px; top: 117px;
    width: 190px; height: 194px;
    background: var(--white);
    border: 2px solid var(--brand-orange);
    text-align: center;
    color: var(--brand-orange);
    font-family: "Roboto Condensed", sans-serif;
  }
  .brand-dot {
    display: block;
    width: 22px; height: 22px; border-radius: 50%;
    background: var(--brand-orange);
    margin: 22px auto 0;
  }
  .kicker {
    margin-top: 14px;
    font-size: 15px; font-weight: 400; line-height: 1.2;
  }
  .fruit-name {
    margin-top: 1px;
    font-size: 25px; font-weight: 700; line-height: 1.2; letter-spacing: 0.3px;
  }
  .brand-name {
    position: absolute; left: 0; right: 0; bottom: 9px;
    font-family: "Roboto", sans-serif;
    font-size: 16px; font-weight: 500;
  }
  .stripe-area {
    position: absolute; left: 0; width: 100%; top: 436px; height: 58px;
    background: linear-gradient(180deg, var(--band-green) 0%, var(--band-yellow) 50%, var(--brand-orange) 100%);
  }
  .footer-band {
    position: absolute; left: 0; bottom: 0; width: 100%; height: 76px;
    background: var(--brand-orange);
    color: var(--white);
    font-family: "Roboto Condensed", sans-serif;
    text-align: center;
  }
  .craft {
    display: inline-block;
    margin-top: 14px; padding: 0 24px 3px;
    border-bottom: 1px solid rgba(255,255,255,0.7);
    font-size: 14px; letter-spacing: 1px;
  }
  .specs {
    display: flex; justify-content: center;
    margin-top: 5px; font-size: 14px;
  }
  .specs span { padding: 0 8px; }
  .specs span + span { border-left: 1px solid rgba(255,255,255,0.7); }
</style>
</head>
<body>
<main class="stage">
  <article class="label">
    <div class="label-body">
      <section class="title-card">
        <span class="brand-dot"></span>
        <p class="kicker">liqueur de</p>
        <h1 class="fruit-name">GRAPPEFRUITS</h1>
        <p class="brand-name">DON VALERIO</p>
      </section>
      <div class="stripe-area" role="img" aria-label="Decorative band of green, yellow and orange stripes"></div>
      <footer class="footer-band">
        <p class="craft">fabrication artisanale</p>
        <p class="specs"><span>swiss made</span><span>21% vol</span><span>500ml</span></p>
      </footer>
    </div>
  </article>
</main>
</body>
</html>
```